Audio Visual company needs WordPress Site re-design

We need a new, simple and sleek redesign of our website, www.vornalisound.com. It is crucial that it is mobile platform friendly! The company emphasis is on commercial sound and video installation.

Examples of what our company does can be found here: http://qelmarview.com/

I am NOT looking for a storefront or an e-commerce site. I would just like an elegant site that describes our services. Perhaps incorporate a sleek showcase into the homepage of projects we have completed. Also would like an elegant menu-bar, perhaps enhance our current site menu or similar.

Here is a link to another site that exhibits the content I am looking for. Their target market is also much like mine.
http://www.haskovelstudio.com/ ........ A polished up version of this site would probably be my ideal site. It has almost EXACTLY the content I am looking for. Exclude the "Printing & signage" category. Needs nicer menus, contact page and project showcase.

Here is another example: http://www.brintolmediaworks.com/ ......... This site has a very nice homepage design with a good layout and feature slider. The site is simple, elegant and to the point.

Target Market(s)

Corporate/commercial business, Educational institutions

Industry/Entity Type

E-Commerce

Font styles to use
Serif
Sans Serif

Requirements
Must have
• Mobile friendly navigation
Nice to have
• HTML5 & CSS3
Should not have
• No Zembric Pulse content. No store templates or e-commerce. We are a service based company not a product sales company

```html
<!DOCTYPE html>
<html lang="en">
<head>
<meta charset="utf-8">
<title>Vornali Sound — Commercial Audio &amp; Video</title>
<link href="https://fonts.googleapis.com/css2?family=Open+Sans:wght@300;400;600;700&display=swap" rel="stylesheet">
<style>
:root{
  --navy:#2a2566;
  --navy-deep:#1f1b52;
  --red:#e0232b;
  --light:#eceeef;
  --white:#ffffff;
  --ink:#3d3d4a;
  --muted:#6f7080;
  --amber:#f0a43a;
}
*{margin:0;padding:0;box-sizing:border-box}
html,body{width:1200px;height:3207px;overflow:hidden}
body{font-family:"Open Sans",Arial,sans-serif;color:var(--ink);background:var(--white);position:relative}
.abs{position:absolute}
p{line-height:1.55}

/* hero */
.hero{top:0;left:0;width:1200px;height:575px;overflow:hidden}
.hero-photo{position:absolute;inset:0;background:linear-gradient(135deg,#7d6f86 0%,#c9b8b8 45%,#e7e1dc 70%,#a99a9e 100%)}
.hero-overlay{position:absolute;inset:0}
.brand{top:42px;left:160px;display:flex;align-items:center;gap:12px;color:var(--white);font-weight:700;font-size:30px;letter-spacing:.5px}
.brand-mark{width:22px;height:22px;background:var(--red)}
.main-nav{top:60px;left:727px;display:flex;gap:0;font-size:13px;color:var(--white)}
.main-nav a{color:var(--white);text-decoration:none;position:absolute;white-space:nowrap}
.main-nav a.is-active{color:var(--red)}
.hero-title{top:170px;left:160px;font-size:31px;font-weight:400;color:var(--white);letter-spacing:.5px}
.hero-title span{color:var(--red)}
.hero-copy{top:238px;left:160px;width:380px;font-size:12px;color:var(--white)}
.hero-copy p{margin-bottom:12px}
.hero-copy .lead{font-size:14px;margin-bottom:16px}
.hero-copy .lead b{color:var(--red);font-weight:400}
.btn-more{top:448px;left:160px;width:155px;height:30px;background:var(--red);color:var(--white);font-size:10px;font-weight:600;text-transform:uppercase;display:flex;align-items:center;justify-content:center;letter-spacing:.3px}
.slider-dots{top:530px;left:165px;display:flex;gap:18px}
.slider-dots i{display:block;width:22px;height:22px;transform:rotate(45deg);background:var(--navy)}
.slider-dots i.on{background:var(--red)}

/* section heads */
.section-head{left:0;width:1200px;background:var(--light);text-align:center}
.section-head h2{font-weight:300;font-size:29px;color:#3a3a46;letter-spacing:.5px}
.section-head .rule{width:600px;height:1px;background:#c5c6cc;margin:8px auto 0;position:relative}
.section-head .rule::after{content:"";position:absolute;left:50%;top:-4px;width:8px;height:8px;margin-left:-4px;background:var(--light);border:1px solid #b5b6bc;transform:rotate(45deg)}
.section-head p{font-size:12px;color:var(--muted);width:720px;margin:22px auto 0}

/* services */
.services{top:753px;left:0;width:1200px;height:530px;display:grid;grid-template-columns:600px 600px;grid-template-rows:265px 265px}
.service{background:var(--navy);color:var(--white);position:relative;border:1px solid rgba(255,255,255,.08)}
.service.is-featured{background:var(--red)}
.service svg{position:absolute;left:227px;top:38px}
.service h3{position:absolute;left:320px;top:38px;font-size:19px;font-weight:400}
.service p{position:absolute;left:200px;top:128px;width:360px;font-size:11px;line-height:1.6}

/* reviews */
.reviews{top:1283px;left:0;width:1200px;height:526px;overflow:hidden}
.reviews-photo{position:absolute;inset:0;background:linear-gradient(180deg,#4a2a1c 0%,#6b3d26 40%,#3c2218 100%)}
.reviews-shade{position:absolute;inset:0;background:rgba(20,10,8,.35)}
.reviews h2{position:absolute;top:35px;width:100%;text-align:center;color:var(--white);font-weight:300;font-size:44px;letter-spacing:1px}
.reviews h2 small{font-size:20px;letter-spacing:2px}
.reviews .rule{position:absolute;top:104px;left:300px;width:600px;height:1px;background:rgba(255,255,255,.5)}
.review-title{position:absolute;top:183px;width:100%;text-align:center;color:var(--amber);font-size:23px}
.review-text{position:absolute;top:236px;left:290px;width:620px;text-align:center;color:var(--white);font-size:11.5px}
.review-date{position:absolute;top:330px;width:100%;text-align:center;color:#d8d0cc;font-size:10px}
.review-arrow{position:absolute;top:242px}

/* partners */
.partners-band{top:1809px;left:0;width:1200px;height:110px;background:var(--navy);color:var(--white);text-align:center}
.partners-band h2{font-weight:400;font-size:28px;letter-spacing:1px;padding-top:4px}
.partners-band p{font-size:11px;width:760px;margin:6px auto 0;line-height:1.5}
.partners-pointer{top:1918px;left:588px}
.partners-row{top:1919px;left:0;width:1200px;height:192px;background:var(--white)}
.partner-badge{position:absolute}

/* works */
.work-tabs{top:2290px;left:0;width:1200px;height:43px;background:var(--white)}
.work-tab{position:absolute;top:0;height:43px;display:flex;align-items:center;font-size:15px;color:#333}
.work-tab.is-active{background:var(--red);color:var(--white);justify-content:center}
.work-grid{top:2333px;left:0;width:1200px;height:171px;display:flex}
.work-item{height:171px;border-right:2px solid #fff}
.work-captions{top:2504px;left:0;width:1200px;height:48px;background:var(--white)}
.work-captions span{position:absolute;top:14px;font-size:11px;color:#333;text-align:center}
.work-captions .is-current{border-bottom:3px solid var(--amber);padding-bottom:8px}

/* contact */
.contact-head{top:2552px;height:115px}
.contact-head h2{font-weight:400;font-size:28px;color:#4a4a55;padding-top:38px}
.contact-pointer{top:2666px;left:584px}
.contact-block{top:2667px;left:0;width:1200px;height:500px;overflow:hidden}
.contact-map{position:absolute;inset:0;background:linear-gradient(160deg,#3a3478 0%,#2e2a6b 50%,#26225c 100%)}
.contact-info{color:var(--white);font-size:12px}
.contact-info h4{font-size:14px;font-weight:700;margin-bottom:4px}
.contact-info p{line-height:1.5}

/* footer */
.site-footer{top:3167px;left:0;width:1200px;height:40px;background:var(--navy-deep);color:#c9c7dd;font-size:10px}
.site-footer .copy{position:absolute;left:200px;top:14px}
.social{position:absolute;top:8px;width:26px;height:26px;background:#4a6fb5}
.social.alt{background:#2c9ad9}
</style>
</head>
<body>

<header class="abs hero">
  <div class="hero-photo" role="img" aria-label="Ceiling-mounted projector installation in a conference room"></div>
  <svg class="hero-overlay" width="1200" height="575" viewBox="0 0 1200 575" aria-hidden="true">
    <polygon points="0,0 710,0 460,575 0,575" fill="#2a2566" fill-opacity="0.9"/>
  </svg>
  <div class="abs brand"><span class="brand-mark"></span>Vornali Sound</div>
  <nav class="abs main-nav">
    <a class="is-active" style="left:0">Home</a>
    <a style="left:48px">Services</a>
    <a style="left:203px">Work</a>
    <a style="left:275px">About</a>
    <a style="left:347px">Contact</a>
  </nav>
  <h1 class="abs hero-title">WELCOME TO <span>VORNALI SOUND</span></h1>
  <div class="abs hero-copy">
    <p class="lead"><b>Vornali Sound</b> has been customizing audio and video</p>
    <p>Clear sound and sharp video for every room. We plan, install and tune systems for offices, schools and venues, keeping each project on time and within budget.</p>
    <p>From one screen to a full campus, our team handles wiring, mounting and calibration so your space simply works.</p>
  </div>
  <div class="abs btn-more">Click more information</div>
  <div class="abs slider-dots"><i></i><i class="on"></i></div>
</header>

<section class="abs section-head" style="top:575px;height:178px">
  <h2 style="padding-top:40px">WHAT WE DO</h2>
  <div class="rule"></div>
  <p>We design and install commercial sound and video systems, tuned to the room and built to last for years of daily use.</p>
</section>

<section class="abs services">
  <article class="service is-featured">
    <svg width="62" height="46" viewBox="0 0 62 46" aria-hidden="true"><rect x="2" y="2" width="58" height="34" fill="none" stroke="#fff" stroke-width="2"/><line x1="20" y1="44" x2="42" y2="44" stroke="#fff" stroke-width="2"/><line x1="31" y1="36" x2="31" y2="44" stroke="#fff" stroke-width="2"/></svg>
    <h3>Digital Media Signage</h3>
    <p>Our team plans digital signage from the first sketch to the final screen. We look at how people move through your space, choose the right displays and content players, and set up a system that is easy to update and clear to read from any distance.</p>
  </article>
  <article class="service">
    <svg width="62" height="60" viewBox="0 0 62 60" aria-hidden="true"><rect x="4" y="2" width="24" height="56" fill="none" stroke="#fff" stroke-width="2"/><circle cx="16" cy="16" r="5" fill="none" stroke="#fff" stroke-width="2"/><circle cx="16" cy="40" r="8" fill="none" stroke="#fff" stroke-width="2"/><rect x="34" y="2" width="24" height="56" fill="none" stroke="#fff" stroke-width="2"/><circle cx="46" cy="16" r="5" fill="none" stroke="#fff" stroke-width="2"/><circle cx="46" cy="40" r="8" fill="none" stroke="#fff" stroke-width="2"/></svg>
    <h3>Live-Sound Integration</h3>
    <p>Whether it's an auditorium, gymnasium, corporate meeting room or a house of worship, Vornali Sound can design and install a state-of-the-art sound system to meet your needs and budget. With years of experience in all types of rooms, indoor and outdoor, we tune the sound where it belongs.</p>
  </article>
  <article class="service">
    <svg width="62" height="50" viewBox="0 0 62 50" aria-hidden="true"><rect x="6" y="18" width="50" height="14" transform="rotate(35 31 25)" fill="none" stroke="#fff" stroke-width="2"/><circle cx="20" cy="17" r="2" fill="#fff"/><circle cx="28" cy="23" r="2" fill="#fff"/><circle cx="36" cy="29" r="2" fill="#fff"/></svg>
    <h3>Universal Remotes</h3>
    <p>Why a universal remote control? Most modern rooms are made of many parts: screens, players, receivers, lights and blinds. A single programmed remote brings them together, so one button starts the meeting, dims the lights and turns on the sound every time.</p>
  </article>
  <article class="service">
    <svg width="62" height="46" viewBox="0 0 62 46" aria-hidden="true"><path d="M4 4 Q31 16 58 4 L58 36 Q31 28 4 36 Z" fill="none" stroke="#fff" stroke-width="2"/><path d="M10 8 L14 40 M52 8 L48 40" stroke="#fff" stroke-width="2"/></svg>
    <h3>Home Theaters</h3>
    <p>What makes a great home theater? Is it the size of the room or the size of the screen? It is the balance of picture, sound and comfort. We listen to how you watch, then plan a room that fits your space and budget and delivers the best result.</p>
  </article>
</section>

<section class="abs reviews">
  <div class="reviews-photo" role="img" aria-label="Interior of a restaurant counter with menu flatscreens installed above"></div>
  <div class="reviews-shade"></div>
  <h2>CUSTOMER <small>REVIEWS</small></h2>
  <div class="rule"></div>
  <div class="review-title">Installation of Flatscreen at Harbor Deli Restaurant</div>
  <p class="review-text">Dalton did an excellent job installing a flatscreen TV at our restaurant. The location we wanted was a difficult one, and he routed all the wires neatly so the finished install looks clean. The result speaks to his care and skill, and I would recommend him for any electronics related work!</p>
  <div class="review-date">Oct 21, 2015 by Mark</div>
  <svg class="review-arrow" style="left:218px" width="30" height="30" viewBox="0 0 30 30" aria-hidden="true"><rect x="6" y="6" width="18" height="18" transform="rotate(45 15 15)" fill="none" stroke="#fff" stroke-width="1.5"/><path d="M17 10 L12 15 L17 20" fill="none" stroke="#fff" stroke-width="2"/></svg>
  <svg class="review-arrow" style="left:947px" width="30" height="30" viewBox="0 0 30 30" aria-hidden="true"><rect x="6" y="6" width="18" height="18" transform="rotate(45 15 15)" fill="none" stroke="#f0a43a" stroke-width="1.5"/><path d="M13 10 L18 15 L13 20" fill="none" stroke="#f0a43a" stroke-width="2"/></svg>
</section>

<section class="abs partners-band">
  <h2>Our Partners</h2>
  <p>We are proud of the level of trust and teamwork we share with our partners. Together we review plans, refine ideas and deliver projects our clients are happy with.</p>
</section>
<svg class="abs partners-pointer" width="24" height="12" viewBox="0 0 24 12" aria-hidden="true"><polygon points="0,0 24,0 12,12" fill="#2a2566"/></svg>
<section class="abs partners-row">
  <svg class="partner-badge" style="left:162px;top:68px" width="40" height="40" viewBox="0 0 40 40" aria-hidden="true"><rect x="8" y="8" width="24" height="24" transform="rotate(45 20 20)" fill="#2a2566"/><path d="M23 14 L16 20 L23 26" fill="none" stroke="#fff" stroke-width="2"/></svg>
  <div class="partner-badge" style="left:246px;top:78px;width:176px;height:50px;background:#2a3f8f"></div>
  <div class="partner-badge" style="left:460px;top:78px;width:192px;height:50px;background:#cc2030"></div>
  <div class="partner-badge" style="left:705px;top:64px;width:112px;height:76px;border-radius:50%;background:#6a9a3a"></div>
  <div class="partner-badge" style="left:860px;top:64px;width:86px;height:78px;background:#f07a24"></div>
  <svg class="partner-badge" style="left:995px;top:68px" width="40" height="40" viewBox="0 0 40 40" aria-hidden="true"><rect x="8" y="8" width="24" height="24" transform="rotate(45 20 20)" fill="#e0232b"/><path d="M17 14 L24 20 L17 26" fill="none" stroke="#fff" stroke-width="2"/></svg>
</section>

<section class="abs section-head" style="top:2111px;height:179px">
  <h2 style="padding-top:30px">LATEST WORKS</h2>
  <div class="rule"></div>
  <p>A selection of recent installations: projectors, screens, speakers and control systems for clients across the region.</p>
</section>
<nav class="abs work-tabs">
  <span class="work-tab is-active" style="left:150px;width:165px">Projectors</span>
  <span class="work-tab" style="left:342px">Flatscreens &amp; Mounts</span>
  <span class="work-tab" style="left:545px">Loudspeakers</span>
  <span class="work-tab" style="left:735px">Microphones</span>
  <span class="work-tab" style="left:900px">Control Systems</span>
</nav>
<div class="abs work-grid">
  <div class="work-item" style="width:147px;background:linear-gradient(180deg,#5a5560,#2e2a33)" role="img" aria-label="Home cinema room"></div>
  <div class="work-item" style="width:179px;background:linear-gradient(180deg,#8a8e98,#d8d9de)" role="img" aria-label="Ceiling projector"></div>
  <div class="work-item" style="width:182px;background:linear-gradient(180deg,#2a3a8a,#18205a)" role="img" aria-label="Concert stage lighting"></div>
  <div class="work-item" style="width:179px;background:linear-gradient(180deg,#2a2a30,#101014)" role="img" aria-label="Floor-standing loudspeaker"></div>
  <div class="work-item" style="width:182px;background:linear-gradient(180deg,#3c56a8,#1d2c70)" role="img" aria-label="Stage microphone"></div>
  <div class="work-item" style="width:179px;background:linear-gradient(180deg,#4a6090,#2a3560)" role="img" aria-label="Control panel buttons"></div>
  <div class="work-item" style="width:152px;border-right:0;background:linear-gradient(180deg,#6a4a6a,#3a2848)" role="img" aria-label="Cable patch rack"></div>
</div>
<div class="abs work-captions">
  <span style="left:0;width:147px">Home Cine</span>
  <span class="is-current" style="left:147px;width:179px">Teatre Mints</span>
  <span style="left:326px;width:182px">excenary city</span>
  <span style="left:508px;width:179px">Cleaner App</span>
  <span style="left:687px;width:182px">Logo Design</span>
  <span style="left:869px;width:179px">Institute EUSA</span>
  <span style="left:1048px;width:152px">Cable struct</span>
</div>

<section class="abs section-head contact-head">
  <h2>Do you like what you see? Contact Us</h2>
</section>
<section class="abs contact-block">
  <div class="contact-map" role="img" aria-label="Street map of the office surroundings"></div>
  <svg class="abs" style="left:324px;top:200px" width="22" height="30" viewBox="0 0 22 30" aria-hidden="true"><path d="M11 1 C5 1 1 5.5 1 11 C1 18 11 29 11 29 C11 29 21 18 21 11 C21 5.5 17 1 11 1 Z" fill="#fff"/><circle cx="11" cy="11" r="4" fill="#2e2a6b"/></svg>
  <div class="abs contact-info" style="left:371px;top:194px">
    <h4>Location</h4>
    <p>1180 Larkspur Avenue<br>Ashford</p>
  </div>
  <div class="abs contact-info" style="left:371px;top:278px">
    <h4>Phone</h4>
    <p>(555) 014-2280<br><br>(555) 014-2281</p>
  </div>
  <div class="abs contact-info" style="left:697px;top:194px">
    <h4>Email</h4>
    <p>info@vornalisound.com</p>
  </div>
</section>
<svg class="abs contact-pointer" style="z-index:2" width="32" height="16" viewBox="0 0 32 16" aria-hidden="true"><polygon points="0,0 32,0 16,16" fill="#eceeef"/></svg>

<footer class="abs site-footer">
  <span class="copy">© 2015 Vornali Sound, All Rights Reserved</span>
  <span class="social" style="left:922px"></span>
  <span class="social alt" style="left:966px"></span>
</footer>

</body>
</html>
```